Harnwick Aerial Services, LLC - Business Card

I currently have a drone business that specializes in aerial photography, thermal image inspections, deer recovery, search and rescue, custom agricultural applications. i will attach my current business card as well as some logos to incorporate for a new up to date business card
Updates

Designs look the same

Sick

Target Market(s)

farmers, hunters

Contact Information for Business Card

name address phone number (as existing card i attached)

Requirements
Must have
• im good with existing business card, but would like an agricultural twist

```html
<!DOCTYPE html>
<html lang="en">
<head>
<meta charset="utf-8">
<title>Harnwick Aerial Services, LLC – Business Card</title>
<link rel="stylesheet" href="https://fonts.googleapis.com/css2?family=Montserrat:wght@400;500;700&display=swap">
<style>
  :root {
    --backdrop: #e0e0e0;
    --card-dark: #3d3d3d;
    --mark-dark: #151515;
    --white: #ffffff;
    --red: #f2232e;
    --text-grey: #555555;
    --blush: #fde1cf;
    --leaf-green: #3f9b3a;
  }
  * { margin: 0; padding: 0; box-sizing: border-box; }
  html, body { width: 1200px; height: 1200px; overflow: hidden; }
  body {
    background: var(--backdrop);
    font-family: "Montserrat", Arial, sans-serif;
    position: relative;
  }
  .card {
    position: absolute;
    left: 179px;
    width: 861px;
    height: 496px;
    overflow: hidden;
  }
  /* Front */
  .card-front { top: 84px; background: var(--card-dark); }
  .front-brand {
    position: absolute;
    left: 0; right: 0; top: 200px;
    display: flex; align-items: center; justify-content: center; gap: 22px;
  }
  .front-brand-dot {
    width: 62px; height: 62px;
    border-radius: 50%;
    background: var(--mark-dark);
  }
  .front-brand-name {
    font-weight: 700;
    font-size: 64px;
    letter-spacing: 6px;
    color: var(--mark-dark);
    text-transform: uppercase;
  }
  /* Back */
  .card-back { top: 621px; background: var(--white); }
  .band-line {
    position: absolute; left: 0; right: 0;
    background: var(--red);
  }
  .band-line.top { top: 66px; height: 5px; }
  .band-line.main { top: 75px; height: 80px; }
  .band-line.bottom { top: 159px; height: 6px; }
  .brand-seal {
    position: absolute;
    left: 66px; top: 37px;
    width: 168px; height: 168px;
    border-radius: 50%;
    background: var(--white);
    display: flex; align-items: center; justify-content: center;
  }
  .brand-seal-name {
    font-weight: 700;
    font-size: 22px;
    letter-spacing: 1px;
    color: var(--leaf-green);
    text-transform: uppercase;
  }
  .holder {
    position: absolute;
    right: 11px; top: 84px;
    text-align: right;
  }
  .holder-name {
    font-weight: 700;
    font-size: 30px;
    letter-spacing: 3px;
    color: var(--white);
    text-transform: uppercase;
    line-height: 34px;
  }
  .holder-role {
    font-weight: 700;
    font-size: 25px;
    letter-spacing: 1px;
    color: var(--blush);
    line-height: 30px;
  }
  .services {
    position: absolute;
    left: 17px; top: 222px;
    list-style: none;
  }
  .service {
    display: flex; align-items: center;
    height: 38px; margin-bottom: 20px;
    font-size: 27px;
    color: var(--text-grey);
  }
  .service svg { width: 32px; height: 34px; margin-right: 14px; fill: var(--red); }
  .contact {
    position: absolute;
    right: 11px; top: 222px;
    text-align: right;
    color: var(--text-grey);
    font-size: 26px;
    letter-spacing: 3px;
  }
  .address p { line-height: 37px; }
  .contact-lines { margin-top: 28px; }
  .contact-line {
    display: flex; justify-content: flex-end; align-items: center;
    line-height: 37px;
  }
  .contact-line svg {
    width: 26px; height: 26px; margin-left: 12px;
    fill: none; stroke: var(--red); stroke-width: 2.4;
  }
  .footer-bar {
    position: absolute; left: 0; right: 0; bottom: 0;
    height: 11px; background: var(--red);
  }
</style>
</head>
<body>

<section class="card card-front">
  <div class="front-brand">
    <span class="front-brand-dot"></span>
    <span class="front-brand-name">Harnwick</span>
  </div>
</section>

<section class="card card-back">
  <div class="band-line top"></div>
  <div class="band-line main"></div>
  <div class="band-line bottom"></div>

  <div class="brand-seal">
    <span class="brand-seal-name">Harnwick</span>
  </div>

  <div class="holder">
    <p class="holder-name">Wesley Harnwick</p>
    <p class="holder-role">Owner</p>
  </div>

  <ul class="services">
    <li class="service"><svg viewBox="0 0 32 34"><polygon points="0,0 32,17 0,34"/></svg>Thermal Image Inspections</li>
    <li class="service"><svg viewBox="0 0 32 34"><polygon points="0,0 32,17 0,34"/></svg>Real Estate Photography</li>
    <li class="service"><svg viewBox="0 0 32 34"><polygon points="0,0 32,17 0,34"/></svg>Deer Recovery</li>
    <li class="service"><svg viewBox="0 0 32 34"><polygon points="0,0 32,17 0,34"/></svg>Search &amp; Rescue</li>
  </ul>

  <div class="contact">
    <div class="address">
      <p>214 E. Market St.</p>
      <p>Delmont OH 45890</p>
    </div>
    <div class="contact-lines">
      <p class="contact-line">419 555 0142
        <svg viewBox="0 0 24 24"><path d="M6 3l3 4-2 2c1 3 4 6 7 7l2-2 4 3-2 4C10 21 3 14 3 5z"/><path d="M14 3a7 7 0 0 1 7 7M14 7a3 3 0 0 1 3 3"/></svg>
      </p>
      <p class="contact-line">harnwickaerial@mail.com
        <svg viewBox="0 0 24 24"><rect x="2" y="5" width="20" height="14"/><path d="M2 5l10 8 10-8M2 19l7-7M22 19l-7-7"/></svg>
      </p>
      <p class="contact-line">www.harnwickaerial.com
        <svg viewBox="0 0 24 24"><circle cx="12" cy="12" r="10"/><ellipse cx="12" cy="12" rx="4.5" ry="10"/><path d="M2 12h20M4 7h16M4 17h16"/></svg>
      </p>
    </div>
  </div>

  <div class="footer-bar"></div>
</section>

</body>
</html>
```